Business Card Tevan Law llc examples and ideas are attached.

in addition to the logo we need a desription what we do: "Reprsenting students with disabilites obtain services to progress in the public school system."

If you can squeeze it on the fron at the bottom great if not put it on the back

```html
<!DOCTYPE html>
<html lang="en">
<head>
<meta charset="utf-8">
<title>Tevan Law llc – Business Card</title>
<link rel="stylesheet" href="https://fonts.googleapis.com/css2?family=Open+Sans:wght@400;600;700&display=swap">
<style>
  :root {
    --navy: #152a4a;
    --navy-deep: #0f1f38;
    --gold: #c9a23a;
    --gold-light: #e6c766;
    --paper: #f1f2f4;
    --paper-shade: #d9dce1;
    --ink: #1c2f4f;
    --stage: #e7e5e1;
  }
  * { box-sizing: border-box; margin: 0; padding: 0; }
  html, body { width: 1200px; height: 800px; overflow: hidden; }
  body {
    background: var(--stage);
    font-family: "Open Sans", Arial, sans-serif;
    display: flex;
    align-items: center;
    justify-content: center;
    gap: 40px;
  }
  .card {
    width: 540px;
    height: 309px;
    position: relative;
    overflow: hidden;
    border-radius: 4px;
    box-shadow: 0 6px 18px rgba(0,0,0,.18);
  }

  /* Back side */
  .card-back {
    background: linear-gradient(160deg, var(--navy) 0%, var(--navy-deep) 100%);
    display: flex;
    flex-direction: column;
    align-items: center;
    justify-content: center;
    color: var(--gold);
    text-align: center;
  }
  .back-mark {
    width: 74px;
    height: 74px;
    border: 4px solid var(--gold);
    margin-bottom: 18px;
  }
  .back-name {
    font-size: 30px;
    font-weight: 600;
    color: var(--gold);
    margin-bottom: 30px;
  }
  .back-mission {
    font-size: 11.5px;
    letter-spacing: 2px;
    text-transform: uppercase;
    color: #cfd6e2;
    line-height: 1.6;
    max-width: 470px;
  }

  /* Front side */
  .card-front {
    background: linear-gradient(135deg, #fafbfc 0%, var(--paper) 45%, var(--paper-shade) 100%);
  }
  .front-surface {
    position: absolute;
    inset: 0 0 52px 0;
  }
  .front-mark {
    position: absolute;
    left: 48px;
    top: 54px;
    width: 136px;
    height: 136px;
    border: 10px solid var(--navy);
  }
  .front-info {
    position: absolute;
    left: 228px;
    top: 34px;
    color: var(--ink);
  }
  .firm-name {
    font-size: 30px;
    font-weight: 600;
    color: var(--navy);
    margin-bottom: 14px;
  }
  .person-name {
    font-size: 17px;
    font-weight: 700;
    line-height: 1.1;
  }
  .person-title {
    font-size: 10px;
    margin-bottom: 8px;
  }
  .contact-row {
    display: flex;
    align-items: flex-start;
    gap: 7px;
    font-size: 12.5px;
    line-height: 1.3;
  }
  .contact-row svg { flex: none; margin-top: 2px; }
  .contact-group { margin-bottom: 8px; }
  .front-band {
    position: absolute;
    left: 0; right: 0; bottom: 0;
    height: 52px;
    background: var(--navy);
    border-top: 4px solid var(--gold);
  }
  .front-band::before {
    content: "";
    position: absolute;
    left: 0; right: 0; top: 6px;
    height: 1px;
    background: var(--gold-light);
    opacity: .6;
  }
</style>
</head>
<body>

  <section class="card card-back" aria-label="Business card back">
    <div class="back-mark" aria-hidden="true"></div>
    <div class="back-name">Tevan Law llc</div>
    <p class="back-mission">Reprsenting students with disabilites obtain services<br>to progress in the public school system</p>
  </section>

  <section class="card card-front" aria-label="Business card front">
    <div class="front-surface"></div>
    <div class="front-mark" aria-hidden="true"></div>
    <div class="front-info">
      <div class="firm-name">Tevan Law llc</div>
      <div class="person-name">Daniel R Tevan</div>
      <div class="person-title">Attorney at Law</div>

      <div class="contact-row contact-group">
        <svg width="12" height="14" viewBox="0 0 12 14" aria-hidden="true">
          <path d="M6 0a4.5 4.5 0 0 0-4.5 4.5C1.5 8 6 12 6 12s4.5-4 4.5-7.5A4.5 4.5 0 0 0 6 0zm0 6.3A1.8 1.8 0 1 1 6 2.7a1.8 1.8 0 0 1 0 3.6z" fill="var(--navy)"/>
          <ellipse cx="6" cy="13" rx="5" ry="1" fill="var(--navy)"/>
        </svg>
        <div>1450 Harbor View Rd<br>Coral Bay FL 33410<br>By appointment only</div>
      </div>

      <div class="contact-row">
        <svg width="12" height="12" viewBox="0 0 12 12" aria-hidden="true">
          <path d="M2.4 0.5l2 2.4-1.1 1.4a7 7 0 0 0 4.4 4.4l1.4-1.1 2.4 2-1.3 1.9C5 11.5 0.5 7 0.5 1.8z" fill="var(--navy)"/>
        </svg>
        <div>555 210 4471</div>
      </div>
      <div class="contact-row">
        <svg width="13" height="11" viewBox="0 0 13 11" aria-hidden="true">
          <rect x="0.5" y="1.5" width="12" height="9" rx="1" fill="var(--navy)"/>
          <path d="M1 2l5.5 4.5L12 2" stroke="#fff" stroke-width="1.2" fill="none"/>
        </svg>
        <div>dan.tevanlaw@example.com</div>
      </div>
    </div>
    <div class="front-band"></div>
  </section>

</body>
</html>
```